Brightwave Travel and Tours

Hotel Reservations
Airline Ticketing
Day Tour

My business is a Travel agency. My services are issuing domestic and international tickets. Book room/hotel reservations local/international.
My color preference is apple green/orange/red/blue.
Images of beaches, tickets,luggage.

```html
<!DOCTYPE html>
<html lang="en">
<head>
<meta charset="utf-8">
<title>Brightwave Travel and Tours – Business Card</title>
<link rel="stylesheet" href="https://fonts.googleapis.com/css2?family=Roboto+Condensed:wght@400;700&family=Roboto:wght@400&display=swap">
<style>
  :root {
    --stage: #000000;
    --sky-top: #6fcbf2;
    --sky-mid: #b5e3f7;
    --haze: #ffffff;
    --sea: #3fb3c4;
    --sea-light: #a9dde3;
    --sand: #e9e6e4;
    --brand-blue: #1d6c92;
    --accent-blue: #1a86d0;
    --ink: #111111;
    --muted: #6f6f6f;
    --hotel-green: #9cc93b;
    --air-orange: #fbbb12;
    --tour-magenta: #b5248a;
  }
  * { margin: 0; padding: 0; box-sizing: border-box; }
  html, body { width: 1200px; height: 1000px; overflow: hidden; background: var(--stage); }
  body { position: relative; font-family: "Roboto Condensed", Arial, sans-serif; }

  .card {
    position: absolute; left: 218px; width: 764px; height: 424px; overflow: hidden;
    background: linear-gradient(180deg, var(--sky-top) 0%, var(--sky-mid) 45%, var(--haze) 74%, var(--haze) 77%);
  }
  .card--front { top: 67px; }
  .card--back { top: 499px; }

  .beach {
    position: absolute; left: 0; right: 0; bottom: 0; height: 108px;
    background: linear-gradient(180deg,
      #f4f7f8 0%, #8fc7d3 8%, var(--sea) 16%, #57c0cc 26%,
      var(--sea-light) 36%, #ffffff 46%, #e3eef0 54%, var(--sand) 66%, #eeebea 100%);
  }

  /* Front */
  .brand {
    position: absolute; left: 82px; top: 100px; width: 250px;
    display: flex; flex-direction: column; align-items: center;
    color: var(--brand-blue); font-weight: 700; text-transform: uppercase; line-height: 1;
  }
  .brand__dot {
    width: 70px; height: 70px; border-radius: 50%; background: var(--brand-blue); margin-bottom: 20px;
  }
  .brand__name { font-size: 38px; letter-spacing: 1px; }
  .brand__tag { font-size: 19px; letter-spacing: 1.5px; margin-top: 4px; }

  .contact { position: absolute; left: 441px; top: 126px; }
  .contact__name { font-size: 35px; font-weight: 700; color: var(--ink); line-height: 1; margin-bottom: 30px; }
  .contact__line { font-size: 22px; color: var(--muted); line-height: 29px; }
  .contact__key { color: var(--accent-blue); font-weight: 700; margin-right: 4px; }

  /* Back */
  .services { position: absolute; left: 0; right: 0; top: 112px; }
  .service { position: absolute; width: 180px; text-align: center; }
  .service--hotel { left: 99px; }
  .service--air { left: 298px; }
  .service--tour { left: 496px; }
  .service__badge {
    width: 100px; height: 100px; margin: 0 auto; border: 2px solid #fff; border-radius: 6px;
    display: flex; align-items: center; justify-content: center;
  }
  .service--hotel .service__badge { background: var(--hotel-green); }
  .service--air .service__badge { background: var(--air-orange); }
  .service--tour .service__badge { background: var(--tour-magenta); }
  .service__label { margin-top: 12px; font-size: 20px; color: var(--ink); }
  .services__note {
    position: absolute; left: 0; right: 0; top: 268px; text-align: center;
    font-family: "Roboto", Arial, sans-serif; font-size: 13.5px; color: var(--ink);
  }
</style>
</head>
<body>

<section class="card card--front">
  <div class="brand">
    <span class="brand__dot"></span>
    <span class="brand__name">Brightwave</span>
    <span class="brand__tag">Travel and Tours</span>
  </div>
  <div class="contact">
    <p class="contact__name">Name Name</p>
    <p class="contact__line">Address Line 1, Line 2,</p>
    <p class="contact__line"><span class="contact__key">P</span>055 555 555</p>
    <p class="contact__line"><span class="contact__key">E</span>contact@brightwave.com</p>
  </div>
  <div class="beach" role="img" aria-label="Photo of a calm turquoise sea meeting a white sandy beach"></div>
</section>

<section class="card card--back">
  <div class="services">
    <div class="service service--hotel">
      <div class="service__badge">
        <svg width="72" height="50" viewBox="0 0 72 50" aria-hidden="true">
          <rect x="2" y="4" width="6" height="44" fill="#000"/>
          <rect x="2" y="30" width="68" height="8" fill="#000"/>
          <rect x="64" y="20" width="6" height="28" fill="#000"/>
          <circle cx="17" cy="22" r="6" fill="#000"/>
          <rect x="26" y="17" width="36" height="11" rx="3" fill="#000"/>
        </svg>
      </div>
      <p class="service__label">Hotel Reservations</p>
    </div>
    <div class="service service--air">
      <div class="service__badge">
        <svg width="66" height="66" viewBox="0 0 24 24" aria-hidden="true">
          <path fill="#000" d="M21 16v-2l-8-5V3.5a1.5 1.5 0 0 0-3 0V9l-8 5v2l8-2.5V19l-2 1.5V22l3.5-1 3.5 1v-1.5L13 19v-5.5z" transform="rotate(45 12 12)"/>
        </svg>
      </div>
      <p class="service__label">Airline Ticketing</p>
    </div>
    <div class="service service--tour">
      <div class="service__badge">
        <svg width="56" height="62" viewBox="0 0 56 62" aria-hidden="true">
          <rect x="20" y="4" width="16" height="10" rx="3" fill="none" stroke="#000" stroke-width="4"/>
          <rect x="6" y="14" width="44" height="40" rx="5" fill="#000"/>
          <circle cx="14" cy="58" r="3.5" fill="#000"/>
          <circle cx="42" cy="58" r="3.5" fill="#000"/>
        </svg>
      </div>
      <p class="service__label">Day Tour</p>
    </div>
    <p class="services__note">Domestic and International Tickets. Book Room/Hotel Reservations Local/International.</p>
  </div>
  <div class="beach" role="img" aria-label="Photo of a calm turquoise sea meeting a white sandy beach"></div>
</section>

</body>
</html>
```